Flyer für Hausreinigung
Zielgruppe
Hausverwaltungen, Hausbesitzer.
Aufgabenstellung
Ergebnis soll ein Winword-Dokument mit einem Firmenlogo (Vorschlag: Tintenklecks hellgrün/blau verlaufend mit orangem Besen/Wischer/oder Hand - andere Ideen sind willkommen!) sein, das ich noch um Firmenname/Adresse bzw. Empfängerdaten noch vervollständigen/individualisieren kann. Es soll bunt, aber nicht überladen sein, eventuell mit Stockfotos von lachenden/glücklich schauenden aktiven Menschen sein, jung dynamisch aber nicht flippig. Folgender Text sollte darin vorkommen, Umformulierungen und andere Ideen sind hochwillkommen:
Unser Ziel ist es eine Hausbetreuung fast wie ein Hausbesorger zu leisten, jedoch mit zusätzlichen Vorteilen:
· Der Vertrag ist jederzeit ohne Frist kündbar, ohne Angabe von Gründen!
· Reinigung 1 x pro Woche sowie zusätzliche Bedarfsreinigung
· Krankheits- und Urlaubsvertretung sind bereits inklusive.
· Haftpflichtversicherung über 1,5 Mio. Euro
· Inklusive Gartenbetreuung, Garage, Dachboden, Haustechnik
· Kontrollgänge, 7 x 24 h Erreichbarkeit für Mieter und Eigentümer, Handwerkerüberwachung, Notfallkoordination
· Winterbetreuung der Gehsteige täglich mindestens zwischen 6:00 und 22:00
· Inklusive aller Hilfsmittel und Materialien
· Fixpreis pro Monat.
Nach Möglichkeit soll das auf 1 A4-Seite Platz finden.

```html
<!DOCTYPE html>
<html lang="de">
<head>
<meta charset="utf-8">
<title>Hausbetreuung Anton Berger – Flyer</title>
<link rel="stylesheet" href="https://fonts.googleapis.com/css2?family=PT+Sans:ital,wght@0,400;0,700;1,700&display=swap">
<style>
  :root {
    --ink: #3f3f3f;
    --ink-light: #8a8a8a;
    --orange: #f07a1a;
    --orange-deep: #e0541a;
    --paper: #ffffff;
    --tint: #f2f7f1;
    --photo-brooms: #b78a5e;
    --photo-street: #8d7a6a;
    --photo-bucket: #a9a9a4;
    --photo-winter: #c9d2d0;
  }
  * { margin: 0; padding: 0; box-sizing: border-box; }
  html, body { width: 848px; height: 1200px; overflow: hidden; background: var(--paper); }
  body { font-family: "PT Sans", sans-serif; color: var(--ink); }
  .flyer { position: relative; width: 848px; height: 1200px; overflow: hidden;
    background: radial-gradient(ellipse at 70% 45%, var(--tint), var(--paper) 70%); }

  .brand { position: absolute; left: 70px; top: 70px; display: flex; align-items: center; gap: 14px; }
  .brand-dot { width: 34px; height: 34px; border-radius: 50%; background: var(--orange); }
  .brand-name { font-size: 30px; font-weight: 700; color: var(--orange); }

  .company { position: absolute; right: 55px; top: 40px; text-align: right; }
  .company-kind { font-size: 36px; font-weight: 700; color: var(--ink); line-height: 1.1; }
  .company-name { font-size: 36px; font-weight: 700; color: var(--ink-light); letter-spacing: 7px; line-height: 1.1; margin-right: -7px; }

  .contact { position: absolute; right: 55px; top: 136px; text-align: right;
    font-style: italic; font-weight: 700; font-size: 20px; line-height: 28px; color: var(--ink); }
  .contact .gap { height: 26px; }

  .claim { position: absolute; left: -30px; top: 392px; width: 630px; height: 90px;
    background: linear-gradient(90deg, var(--orange-deep), var(--orange));
    transform: rotate(-8deg); transform-origin: left top;
    border-radius: 0 36px 36px 0; padding: 17px 24px 0 52px;
    color: #fff; font-weight: 700; font-size: 21px; line-height: 28px; white-space: nowrap; }

  .benefits-frame { position: absolute; left: 70px; top: 470px; width: 723px; height: 483px;
    border-left: 4px solid var(--orange); border-bottom: 4px solid var(--orange-deep);
    border-bottom-left-radius: 60px; }
  .benefits { position: absolute; left: 95px; top: 496px; width: 690px; list-style: none;
    font-size: 21px; font-weight: 700; line-height: 30px; }
  .benefits li { position: relative; padding-left: 38px; }
  .benefits li::before { content: "·"; position: absolute; left: 0; font-weight: 700; }

  .photo-strip { position: absolute; left: 0; top: 990px; width: 848px; height: 210px; }
  .photo { position: absolute; }
  .photo-brooms { left: 0; top: 20px; width: 211px; height: 190px; background: linear-gradient(135deg, #d0a276, var(--photo-brooms)); }
  .photo-street { left: 211px; top: 36px; width: 242px; height: 174px; background: linear-gradient(180deg, #a89888, var(--photo-street)); }
  .photo-bucket { left: 466px; top: 36px; width: 107px; height: 108px; background: linear-gradient(180deg, #c4c3bd, var(--photo-bucket)); }
  .photo-winter { left: 586px; top: 14px; width: 262px; height: 196px; background: linear-gradient(180deg, #e1e6e4, var(--photo-winter)); }
</style>
</head>
<body>
<main class="flyer">
  <div class="brand">
    <span class="brand-dot"></span>
    <span class="brand-name">Anton Berger</span>
  </div>

  <header class="company">
    <div class="company-kind">Hausbetreuung</div>
    <div class="company-name">Anton Berger</div>
  </header>

  <address class="contact">
    <div>Glanzweg 7</div>
    <div>88888 Putzau</div>
    <div class="gap"></div>
    <div>Tel: 0987 65 43 21 &nbsp; -0</div>
    <div>Fax: 0987 65 43 21-00</div>
  </address>

  <div class="claim">Unser Ziel ist es eine Hausbetreuung fast wie ein Haus-<br>besorger zu leisten, jedoch mit zusätzlichen Vorteilen:</div>

  <div class="benefits-frame"></div>
  <ul class="benefits">
    <li>Der Vertrag ist jederzeit ohne Frist kündbar, ohne Angabe<br>von Gründen!</li>
    <li>Reinigung 1 x pro Woche sowie zusätzliche Bedarfsreinigung</li>
    <li>Krankheits- und Urlaubsvertretung sind bereits inklusive.</li>
    <li>Haftpflichtversicherung über 1,5 Mio. Euro</li>
    <li>Inklusive Gartenbetreuung, Garage, Dachboden, Haustechnik</li>
    <li>Kontrollgänge, 7 x 24 h Erreichbarkeit für Mieter und<br>Eigentümer, Handwerkerüberwachung, Notfallkoordination</li>
    <li>Winterbetreuung der Gehsteige täglich mindestens zwischen<br>6:00 und 22:00</li>
    <li>Inklusive aller Hilfsmittel und Materialien</li>
    <li>Fixpreis pro Monat.</li>
  </ul>

  <section class="photo-strip">
    <div class="photo photo-brooms" role="img" aria-label="Foto: Besen und Bürsten mit roten Stielen"></div>
    <div class="photo photo-street" role="img" aria-label="Foto: Arbeiter beim Reinigen eines Gehwegs"></div>
    <div class="photo photo-bucket" role="img" aria-label="Foto: Kübel mit Streusplitt und Schaufel"></div>
    <div class="photo photo-winter" role="img" aria-label="Foto: Schneeräumung in verschneiter Straße"></div>
  </section>
</main>
</body>
</html>
```